Business card design needed for rebranded top-end landscaping business

We need a new business card design, incorporating our logo (colours Green #8dc63f and Grey #8a8c8e) and also some options that include the colour dark navy (eg #000040) as our uniforms are navy with white and grey trim.

We are an innovative landscaping company that maintains high-end gardens for meticulous clients. We pride ourselves on our customer service, our professionalism, and our workmanship.

Our business name needs to be easily read and our branding needs to be bold and memorable, without screaming "tradesman"! We prefer clean lines over lots of fine detail.

The design MUST include:
- Business name ("Brambleton Gardenworks")
- Logo (file uploaded)
- Employee name
- Phone number
- Email address
- www.brambletongardenworks.com.au
- Facebook & Instagram logos
- The Turfcraft Guild logo (file uploaded) along with the word "Member"
- Licence "Lic. 618392K"

OPTIONAL inclusions:
- "Creating outdoor spaces for our community to be inspired, refreshed and re-energised"
- "Landscape Maintenance - Irrigation - Arboriculture" (dashes can be replaced with dots or other)
- "Fully qualified, licensed & insured"
- "Residential - Strata - Commercial - Real Estate" (dashes can be replaced with dots or other)

High-end professionals and retirees, real estate agents

Landscaping

See Project description

Sans Serif

Designer to choose colors to be used in the design.

• Must incorporate our logo, and colours Green #8dc63f and Grey #8a8c8e) from the logo, and the colour DARK NAVY (eg #000040).
• The design MUST include:
• - Business name ("Brambleton Gardenworks")
• - Logo (file uploaded)
• - Employee name
• - Phone number
• - Email address
• - www.brambletongardenworks.com.au
• - Facebook & Instagram logos
• - The Turfcraft Guild logo (file uploaded) along with the word "Member"
• - Licence "Lic. 618392K"
• OPTIONAL inclusions:
• - "Creating outdoor spaces for our community to be inspired, refreshed and re-energised"
• - "Landscape Maintenance - Irrigation - Arboriculture" (dashes can be replaced with dots or other)
• - "Fully qualified, licensed & insured"
• - "Residential - Strata - Commercial - Real Estate" (dashes can be replaced with dots or other)

```html
<!DOCTYPE html>
<html lang="en">
<head>
<meta charset="utf-8">
<title>Brambleton Gardenworks – Business Card</title>
<link href="https://fonts.googleapis.com/css2?family=Source+Sans+3:wght@400;600&display=swap" rel="stylesheet">
<style>
  :root {
    --navy: #13135e;
    --navy-deep: #0d0d4a;
    --green: #8dc63f;
    --grey: #8a8c8e;
    --grey-light: #b8babc;
    --stage: #2b2a28;
  }
  * { margin: 0; padding: 0; box-sizing: border-box; }
  html, body { width: 1200px; height: 900px; overflow: hidden; }
  body {
    background: var(--stage);
    font-family: "Source Sans 3", "Segoe UI", sans-serif;
    position: relative;
  }
  .card {
    position: absolute;
    left: 250px;
    width: 700px;
    height: 400px;
    background: radial-gradient(ellipse at 40% 40%, var(--navy) 0%, var(--navy-deep) 100%);
    overflow: hidden;
    box-shadow: 0 12px 30px rgba(0,0,0,.45);
  }
  .card--back { top: 40px; }
  .card--front { top: 460px; }

  .edge-band { position: absolute; left: 0; bottom: 0; width: 100%; height: 22px; }

  /* back */
  .service-list {
    position: absolute; left: 44px; top: 42px; width: 600px;
    list-style: none; color: var(--green); font-size: 19px; line-height: 1.32;
  }
  .service-list li { position: relative; padding-left: 22px; }
  .service-list li::before {
    content: ""; position: absolute; left: 0; top: 8px;
    width: 9px; height: 9px; border-radius: 50%; background: var(--green);
  }
  .guild-mark {
    position: absolute; right: 46px; bottom: 66px;
    display: flex; align-items: center; gap: 12px;
  }
  .guild-mark__square { width: 26px; height: 26px; background: var(--green); }
  .guild-mark__name {
    color: var(--grey); font-size: 24px; letter-spacing: 2px; text-transform: uppercase;
    border-bottom: 1px solid var(--grey); padding-bottom: 2px;
  }

  /* front */
  .employee { position: absolute; left: 54px; top: 44px; }
  .employee__name { color: var(--green); font-size: 30px; font-weight: 600; line-height: 1; }
  .employee__licence {
    color: var(--grey-light); font-size: 12px; margin-top: 4px;
    border-bottom: 2px solid var(--grey); padding-bottom: 3px; width: 80px;
  }
  .contact-list {
    position: absolute; left: 54px; top: 132px;
    list-style: none; color: var(--green); font-size: 15px; line-height: 1.55;
  }
  .contact-list li { display: flex; align-items: center; gap: 10px; }
  .contact-list svg { width: 12px; height: 12px; flex: none; }
  .social { margin-top: 22px; }
  .social__dot { width: 11px; height: 11px; border-radius: 50%; background: var(--grey-light); flex: none; }
  .social__dot + .social__dot { margin-left: -6px; }

  .brand-mark {
    position: absolute; right: 50px; bottom: 70px;
    display: flex; align-items: center; gap: 12px;
  }
  .brand-mark__circle { width: 30px; height: 30px; border-radius: 50%; background: var(--green); }
  .brand-mark__name { color: var(--green); font-size: 28px; font-weight: 600; line-height: 1; }
</style>
</head>
<body>

<section class="card card--back" aria-label="Card back">
  <ul class="service-list">
    <li>Creating outdoor spaces for our community to be inspired, refreshed and re-energised</li>
    <li>Landscape Maintenance | Irrigation | Arboriculture</li>
    <li>Fully qualified, licensed &amp; insured</li>
    <li>Residential | Strata | Commercial | Real Estate</li>
  </ul>
  <div class="guild-mark">
    <span class="guild-mark__square"></span>
    <span class="guild-mark__name">The Turfcraft Guild</span>
  </div>
  <svg class="edge-band" viewBox="0 0 700 22" preserveAspectRatio="none" aria-hidden="true">
    <polygon points="0,0 326,0 318,22 0,22" fill="var(--grey)"/>
    <polygon points="332,0 700,0 700,22 324,22" fill="var(--green)"/>
  </svg>
</section>

<section class="card card--front" aria-label="Card front">
  <div class="employee">
    <div class="employee__name">Alex Marlow</div>
    <div class="employee__licence">Lic. 618392K</div>
  </div>
  <ul class="contact-list">
    <li>
      <svg viewBox="0 0 12 12"><rect x="3" y="0.5" width="6" height="11" rx="1.2" fill="var(--grey-light)"/></svg>
      00 000 0000
    </li>
    <li>
      <svg viewBox="0 0 12 12"><circle cx="6" cy="6" r="5" fill="none" stroke="var(--grey-light)" stroke-width="1.4"/><path d="M1 6h10M6 1c-2.5 3-2.5 7 0 10M6 1c2.5 3 2.5 7 0 10" fill="none" stroke="var(--grey-light)" stroke-width="1"/></svg>
      www.brambletongardenworks.com.au
    </li>
    <li>
      <svg viewBox="0 0 12 12"><rect x="0.5" y="2" width="11" height="8" fill="var(--grey-light)"/><path d="M0.5 2l5.5 4.5L11.5 2" fill="none" stroke="var(--navy)" stroke-width="1"/></svg>
      alex@brambletongardenworks.com.au
    </li>
    <li class="social">
      <span class="social__dot"></span><span class="social__dot"></span>
      brambletongardenworks
    </li>
  </ul>
  <div class="brand-mark">
    <span class="brand-mark__circle"></span>
    <span class="brand-mark__name">Brambleton Gardenworks</span>
  </div>
  <svg class="edge-band" viewBox="0 0 700 22" preserveAspectRatio="none" aria-hidden="true">
    <polygon points="0,0 326,0 318,22 0,22" fill="var(--grey)"/>
    <polygon points="332,0 700,0 700,22 324,22" fill="var(--green)"/>
  </svg>
</section>

</body>
</html>
```